Harrowgate - Pell Corporate PowerPoint Presentation Template

A custom, corporate template that is highly professional, neat/crisp, "serious," and captures/emphasizes the essence of a global, mutli-brand consumer products company that has deep tradition and values family, hard work, performance, innovation, and service to our consumers and retail partners.
The company's roots and headquarters are in Texas. We are a private and family owned since our founding almost 100 years ago. The corporate website is www.hpvcorp-example.com and other branded websites can be accessed from this site.
Our current presentation title page is attached. We believe it to be somewhat stale/out of date and less sophisticated that the image we'd prefer to project. We occasionally add/change logos and will have to adapt the presentation. These presentations must look good printed.
Please contact me with any questions or requests and I will respond very quickly.
Target Market(s)
Corporate Executives
Industry/Entity Type
It Professional
Requirements
Must have
- Sans Serif font (can't select below). Industry is Apparel and Footwear / Consumer Products (can't select below).

```html
<!DOCTYPE html>
<html lang="en">
<head>
<meta charset="utf-8">
<title>Harrowgate - Pell Corporate Presentation Template</title>
<link href="https://fonts.googleapis.com/css2?family=Open+Sans:wght@400;600;700&family=Ubuntu:wght@400;500&family=Arimo:wght@700&display=swap" rel="stylesheet">
<style>
:root{
  --stage:#6b6b6d;
  --navy:#1d4f9c;
  --red:#d0103a;
  --gold:#ffc20e;
  --grey:#bdbdbd;
  --ink:#555;
  --band:#f6f6f6;
  --rule:#d4d4d4;
  --dash:#9a9a9a;
}
*{margin:0;padding:0;box-sizing:border-box}
html,body{width:1200px;height:910px;overflow:hidden;background:var(--stage)}
body{position:relative;font-family:"Open Sans",Arial,sans-serif;color:var(--ink)}
.slide{position:absolute;width:550px;height:412px;background:#fff;overflow:hidden}
.slide-charts{left:39px;top:28px}
.slide-presence{left:610px;top:27px}
.slide-columns{left:34px;top:461px;width:554px;height:415px}
.slide-closing{left:610px;top:463px}

.header{position:absolute;left:0;top:0;right:0;height:62px;background:var(--band);border-bottom:3px solid var(--rule)}
.brand{position:absolute;left:40px;top:23px;display:flex;align-items:center;gap:5px;font-family:"Open Sans",sans-serif;font-weight:700;font-size:10px;color:var(--navy);letter-spacing:.3px}
.brand-mark{width:9px;height:9px;background:var(--navy)}
.header-title{position:absolute;right:62px;top:14px;text-align:center}
.header-title h1{font-family:"Ubuntu",sans-serif;font-weight:400;font-size:19px;color:var(--navy);line-height:1.1}
.header-title p{font-size:8.5px;color:#666;margin-top:2px}

.footer{position:absolute;left:0;right:0;top:386px;height:8px}
.footer .dash-a{position:absolute;left:0;width:490px;top:0;border-top:2px dashed var(--dash)}
.footer .dash-b{position:absolute;left:0;width:490px;top:5px;border-top:2px dashed var(--dash)}
.footer .dash-end{position:absolute;right:0;width:26px;top:0;height:7px;border-top:2px dashed var(--dash);border-bottom:2px dashed var(--dash)}
.page-num{position:absolute;left:507px;top:-3px;font-size:7px;font-weight:600;color:#555}

.pie{position:absolute;left:0;top:0}
.legend-row{position:absolute;left:278px;display:flex;align-items:center;gap:10px}
.legend-pct{font-family:"Open Sans",sans-serif;font-weight:600;font-size:21px;width:44px}
.legend-text h3{font-size:7px;font-weight:700}
.legend-text p{font-size:6.4px;line-height:1.45;color:#555;width:140px}
.pct-grey{color:var(--grey)} .pct-red{color:var(--red)} .pct-navy{color:var(--navy)} .pct-gold{color:var(--gold)}
.chart-note{position:absolute;left:40px;top:320px;width:460px;font-size:6.3px;line-height:2.1;color:#777}

.map-area{position:absolute;left:106px;top:113px;width:396px;height:188px;background:radial-gradient(ellipse at 50% 45%,#1d4f9c 0%,#1d4f9c 55%,#fff 75%);border-radius:8px}
.map-key{position:absolute;left:55px;display:flex;align-items:center;gap:9px;font-size:6.5px;color:#666}
.key-chip{width:20px;height:10px;clip-path:polygon(15% 0,85% 0,100% 50%,85% 100%,15% 100%,0 50%)}
.presence-text{position:absolute;left:44px;top:318px;width:480px;font-size:6.9px;line-height:1.78;color:#333}

.column{position:absolute;top:120px;width:224px}
.column-left{left:38px}
.column-right{left:288px}
.column h2{font-family:"Arimo",Arial,sans-serif;font-weight:700;font-size:11.5px;color:var(--navy);margin-bottom:4px}
.column p{font-size:6.4px;line-height:1.45;text-align:justify;color:#444;margin-bottom:11px}

.closing-bg{position:absolute;inset:0;background:radial-gradient(ellipse at 35% 55%,#b9bcc1 0%,#d7d9dc 45%,#e6e7e9 100%)}
.closing-dash{position:absolute;left:0;right:0;height:8px;border-top:2px dashed var(--dash);border-bottom:2px dashed var(--dash)}
.closing-brand{position:absolute;left:0;right:0;top:160px;display:flex;justify-content:center;align-items:center;gap:8px;font-weight:700;font-size:22px;color:var(--navy);letter-spacing:.5px}
.closing-brand .brand-mark{width:16px;height:16px}
.closing-title{position:absolute;left:0;right:0;top:236px;text-align:center;font-weight:700;font-size:26px;color:#1f3e72;letter-spacing:.3px}
.closing-band{position:absolute;left:0;right:0;bottom:0;height:18px;background:#1e5fa8}
.closing-band span{position:absolute;right:36px;top:4px;font-size:7.5px;color:#fff}
</style>
</head>
<body>

<section class="slide slide-charts">
  <header class="header">
    <div class="brand"><span class="brand-mark"></span>HARROWGATE-PELL</div>
    <div class="header-title"><h1>Bi Chart Slide</h1><p>Lorem ipsum dolor sit amet consectetur</p></div>
  </header>
  <svg class="pie" width="550" height="320" viewBox="0 0 550 320">
    <path d="M134 198 L134 123 A75 75 0 0 1 178.1 258.7 Z" fill="#1d4f9c"/>
    <path d="M134 198 L178.1 258.7 A75 75 0 0 1 73.3 242.1 Z" fill="#ffc20e"/>
    <path d="M134 198 L73.3 242.1 A75 75 0 0 1 73.3 153.9 Z" fill="#c4c4c4"/>
    <path d="M134 198 L73.3 153.9 A75 75 0 0 1 134 123 Z" fill="#d0103a"/>
    <g fill="none" stroke="#888" stroke-width=".8" stroke-dasharray="1.5 1.5">
      <polyline points="124,163 270,163 270,132 270,132 270,132 270,132"/>
      <polyline points="270,132 268,132"/>
      <polyline points="131,163 219,163 219,178 268,178"/>
      <polyline points="80,187 173,187 173,132 268,132"/>
      <polyline points="171,205 220,205 220,226 268,226"/>
      <polyline points="124,276 124,270 268,270"/>
    </g>
    <g fill="#888"><circle cx="124" cy="163" r="2"/><circle cx="80" cy="187" r="2"/><circle cx="171" cy="205" r="2"/><circle cx="124" cy="276" r="2"/><circle cx="268" cy="132" r="1.5"/><circle cx="268" cy="178" r="1.5"/><circle cx="268" cy="226" r="1.5"/><circle cx="268" cy="270" r="1.5"/></g>
    <g font-family="Open Sans, sans-serif" font-weight="700" font-size="10" fill="#fff">
      <text x="105" y="170">15%</text><text x="69" y="210">20%</text>
      <text x="176" y="229">40%</text><text x="114" y="244">25%</text>
    </g>
  </svg>
  <div class="legend-row" style="top:118px"><span class="legend-pct pct-grey">20%</span><div class="legend-text"><h3 class="pct-grey">Title Goes Here</h3><p>There are many variations of passages of Lorem Ipsum available .</p></div></div>
  <div class="legend-row" style="top:166px"><span class="legend-pct pct-red">15%</span><div class="legend-text"><h3 class="pct-red">Title Goes Here</h3><p>There are many variations of passages of Lorem Ipsum available.</p></div></div>
  <div class="legend-row" style="top:215px"><span class="legend-pct pct-navy">40%</span><div class="legend-text"><h3 class="pct-navy">Title Goes Here</h3><p>There are many variations of passages of Lorem Ipsum available</p></div></div>
  <div class="legend-row" style="top:259px"><span class="legend-pct pct-gold">25%</span><div class="legend-text"><h3 class="pct-gold">Title Goes Here</h3><p>There are many variations of passages of Lorem Ipsum available</p></div></div>
  <p class="chart-note">Lorem ipsum dolor sit amet, <b><i>consectetur adipiscing elit.</i></b> Praesent sodales odio sit amet odio tristique quis tempus odio Lorem ipsum dolor sit amet, consectetur adipiscing elit. Lorem ipsum dolor sit amet, consectetur adipiscing elit. Praesent sodales odio sit amet odio tristique quis tempus odio Lorem ipsum dolor sit amet, consectetur adipiscing elit. Lorem ipsum dolor sit amet, consectetur adipiscing elit.</p>
  <div class="footer"><div class="dash-a"></div><div class="dash-b"></div><span class="page-num">7</span><div class="dash-end"></div></div>
</section>

<section class="slide slide-presence">
  <header class="header">
    <div class="brand"><span class="brand-mark"></span>HARROWGATE-PELL</div>
    <div class="header-title"><h1>Global Presence</h1><p>Lorem ipsum dolor sit amet consectetur</p></div>
  </header>
  <div class="map-area" role="img" aria-label="World map in navy with red and yellow location markers across continents"></div>
  <div class="map-key" style="top:209px"><span class="key-chip" style="background:var(--red)"></span>Area 100%</div>
  <div class="map-key" style="top:231px"><span class="key-chip" style="background:var(--gold)"></span>Area 100%</div>
  <p class="presence-text">Harrowgate-Pell fuels our global growth by focusing on product excellence and maintaining a tireless dedication to superior performance. To secure our position as a global leader in full-service workwear solutions, and to accommodate growing global demand, we've established a multi-continent presence and global distribution capabilities. We've also leveraged strategic partnerships and acquired companies known for product innovation and excellence in workwear: Vander Mill, Forgeline, Ridgecrest and Tallowbrook.</p>
  <div class="footer"><div class="dash-a"></div><div class="dash-b"></div><span class="page-num">9</span><div class="dash-end"></div></div>
</section>

<section class="slide slide-columns">
  <header class="header">
    <div class="brand"><span class="brand-mark"></span>HARROWGATE-PELL</div>
    <div class="header-title"><h1>Two Column text</h1><p>Lorem ipsum dolor sit amet consectetur</p></div>
  </header>
  <div class="column column-left">
    <h2>Title Goes Here</h2>
    <p>There are many variations of passages of lorem ipsum available, but the majority have suffered alteration in some form, by injected humour, or randomized words which don't look even slightly believable. If you are going to use A passage of lorem ipsum, you need to be sure there isn't anything embarrassing hidden in the middle of text. All the lorem ipsum generators.</p>
    <p>If you are going to use a passage of Lorem Ipsum, you need to be sure there isn't anything embarrassing hidden in the middle of text. All the Lorem Ipsum generators on the Internet tend to repeat predefined chunks as necessary, making this the first true generator on the Internet.</p>
    <p>It uses a dictionary of over 200 Latin words, combined with a handful of model sentence structures, to generate Lorem Ipsum which looks reasonable. The generated Lorem Ipsum is therefore always free from repetition, injected humour, or non-characteristic words etc.</p>
    <p>It uses a dictionary of over 200 Latin words, combined with a handful of model sentence structures, to generate Lorem Ipsum which looks reasonable. The generated Lorem Ipsum is therefore always free from repetition, injected humour, or non-characteristic words etc.</p>
  </div>
  <div class="column column-right">
    <h2>Title Goes Here</h2>
    <p>There are many variations of passages of lorem ipsum available, but the majority have suffered alteration in some form, by injected humour, or randomized words which don't look even slightly believable. If you are going to use A passage of lorem ipsum, you need to be sure there isn't anything embarrassing hidden in the middle of text. All the lorem ipsum generators.</p>
    <p>If you are going to use a passage of Lorem Ipsum, you need to be sure there isn't anything embarrassing hidden in the middle of text. All the Lorem Ipsum generators on the Internet tend to repeat predefined chunks as necessary, making this the first true generator on the Internet.</p>
    <p>It uses a dictionary of over 200 Latin words, combined with a handful of model sentence structures, to generate Lorem Ipsum which looks reasonable. The generated Lorem Ipsum is therefore always free from repetition, injected humour, or non-characteristic words etc.</p>
    <p>It uses a dictionary of over 200 Latin words, combined with a handful of model sentence structures, to generate Lorem Ipsum which looks reasonable. The generated Lorem Ipsum is therefore always free from repetition, injected humour, or non-characteristic words etc.</p>
  </div>
  <div class="footer" style="top:389px"><div class="dash-a"></div><div class="dash-b"></div><span class="page-num">11</span><div class="dash-end"></div></div>
</section>

<section class="slide slide-closing">
  <div class="closing-bg" role="img" aria-label="Soft faded photograph of a sewing machine stitching fabric"></div>
  <div class="closing-dash" style="top:30px"></div>
  <div class="closing-dash" style="top:366px"></div>
  <div class="closing-brand"><span class="brand-mark"></span>HARROWGATE-PELL</div>
  <h2 class="closing-title">THANKS FOR WATCHING</h2>
  <div class="closing-band"><span>www.hpvcorp-example.com</span></div>
</section>

</body>
</html>
```